New Business Card for Casual Beachfront Cafe

Quirky Beachfront Cafe at Moana, South Australia needs a DOUBLE SIDED business card to print on PrintHarbor.

Target Market(s)

Business Cards sit on the counter for Guests to take with them. Please view our website www.saltreefcafe.com.au to get a feel for the Cafe. You may also view our Instagram at @saltreefcafe

Industry/Entity Type

Cafe / Restaurant

Contact Information for Business Card

Information equivalent to: Breakfast, Lunch, Dinner, Coffee, Takeaway / 117 Parade Saltmere SX 5990 / Menu & Opening Hours: www.saltreefcafe.com.au / ph (08) 8461 9273

Requirements
Must have
• Information equivalent to: Breakfast, Lunch, Dinner, Coffee, Takeaway / 117 Parade Saltmere SX 5990 / Menu & Opening Hours: www.saltreefcafe.com.au / ph (08) 8461 9273
Nice to have
• Potentially some of our trademark colours (Cafe can be searched via Seekly)
Should not have
• Must NOT have image of the building. May have the logo provided on one side but not necessarily, depending on how you wish to design the card

```html
<!DOCTYPE html>
<html lang="en">
<head>
<meta charset="utf-8">
<title>Salt Reef Cafe – Business Card</title>
<link rel="stylesheet" href="https://fonts.googleapis.com/css2?family=Alegreya:wght@400;700;800&family=Alegreya+Sans:wght@800&display=swap">
<style>
  :root {
    --backdrop: #2e2e2e;
    --teal: #2b5b62;
    --paper: #ffffff;
    --sun: #f8f400;
  }
  * { box-sizing: border-box; margin: 0; padding: 0; }
  html, body { width: 1200px; height: 1056px; overflow: hidden; }
  body {
    background: var(--backdrop);
    position: relative;
    font-family: "Alegreya", Georgia, serif;
  }
  .card {
    position: absolute;
    left: 322px;
    width: 556px;
    height: 318px;
  }
  .card--front { top: 150px; background: var(--paper); color: var(--teal); }
  .card--back  { top: 588px; background: var(--teal); }

  .card__frame {
    position: absolute;
    inset: 20px;
    border: 2px dashed var(--teal);
  }
  .brand-block {
    position: absolute;
    top: 12px;
    left: 50%;
    transform: translateX(-50%);
    width: 158px;
    height: 80px;
    background: var(--teal);
    color: var(--paper);
    display: flex;
    flex-direction: column;
    align-items: center;
    justify-content: center;
    font-weight: 800;
    text-transform: uppercase;
    line-height: 1;
  }
  .brand-block__top { font-size: 20px; letter-spacing: 1px; }
  .brand-block__bottom { font-size: 30px; letter-spacing: 1px; }

  .services {
    position: absolute;
    top: 98px;
    left: 0; right: 0;
    text-align: center;
    font-weight: 800;
    font-size: 26px;
    line-height: 29px;
  }
  .ribbon {
    position: absolute;
    top: 166px;
    left: 78px;
    width: 400px;
    height: 36px;
  }
  .ribbon svg { position: absolute; inset: 0; width: 100%; height: 100%; }
  .ribbon__text {
    position: relative;
    display: block;
    text-align: center;
    line-height: 36px;
    color: var(--paper);
    font-weight: 700;
    font-size: 18px;
  }
  .contact {
    position: absolute;
    top: 210px;
    left: 0; right: 0;
    text-align: center;
  }
  .contact__label { font-weight: 800; font-size: 12px; }
  .contact__web { font-size: 15px; letter-spacing: 4px; margin-top: 1px; }
  .contact__phone {
    font-family: "Alegreya Sans", Arial, sans-serif;
    font-weight: 800;
    font-size: 22px;
    margin-top: 2px;
  }

  .back-brand {
    position: absolute;
    inset: 0;
    display: flex;
    align-items: center;
    justify-content: center;
    gap: 14px;
  }
  .back-brand__mark {
    width: 22px; height: 22px;
    background: var(--sun);
  }
  .back-brand__name {
    color: var(--paper);
    font-weight: 800;
    font-size: 40px;
    text-transform: uppercase;
    letter-spacing: 1px;
  }
</style>
</head>
<body>
  <section class="card card--front" aria-label="Business card front">
    <div class="card__frame"></div>
    <div class="brand-block">
      <span class="brand-block__top">Salt Reef</span>
      <span class="brand-block__bottom">Cafe</span>
    </div>
    <p class="services">•Breakfast • Lunch • Dinner<br>• Coffee • Takeaway</p>
    <div class="ribbon">
      <svg viewBox="0 0 400 36" preserveAspectRatio="none" aria-hidden="true">
        <polygon points="0,0 400,0 384,18 400,36 0,36 16,18" fill="var(--teal)"/>
      </svg>
      <span class="ribbon__text">117 Parade Saltmere SX 5990</span>
    </div>
    <div class="contact">
      <p class="contact__label">Menu &amp; Opening Hours:</p>
      <p class="contact__web">www.saltreefcafe.com.au</p>
      <p class="contact__phone">ph (08) 8461 9273</p>
    </div>
  </section>

  <section class="card card--back" aria-label="Business card back">
    <div class="back-brand">
      <span class="back-brand__mark"></span>
      <span class="back-brand__name">Salt Reef Cafe</span>
    </div>
  </section>
</body>
</html>
```